Business Card Design Project - Tall Maple

We are looking for a new business card design. Our company name is Tall Maple Communication Solutions. Our primary function is to provide our clients with communication solutions. These solutions include commercial phone systems and T1 and Fiber Internet lines. Another major part of the business is cabling new buildings with CAT5 cable for both data and phone.

Industry/Entity Type

Communication

Requirements
Must have
• The cards need to be two sided and have some bleeding edge color.
Nice to have
• We are going to upload our current logo BUT we are not married to this logo. If you want to incorporate a re-designed logo with the new business card - please feel free to do so. We are looking for a new bold look that is very colorful yet professional.

```html
<!DOCTYPE html>
<html lang="en">
<head>
<meta charset="utf-8">
<title>Tall Maple Communication Solutions – Business Card</title>
<link rel="stylesheet" href="https://fonts.googleapis.com/css2?family=Libre+Baskerville:wght@700&family=Arimo&display=swap">
<style>
  :root {
    --navy: #1b2585;
    --grey: #7a7a7a;
    --grey-dark: #555555;
    --paper: #ffffff;
    --backdrop: #eef0f4;
  }
  * { margin: 0; padding: 0; box-sizing: border-box; }
  html, body { width: 1200px; height: 900px; overflow: hidden; }
  body { background: var(--backdrop); position: relative; }

  .card {
    position: absolute;
    background: var(--paper);
    box-shadow: 0 2px 10px rgba(0,0,0,0.18);
    overflow: hidden;
  }

  /* Front */
  .card--front { left: 60px; top: 260px; width: 580px; height: 375px; }
  .card--front .corners { position: absolute; inset: 0; }
  .brand {
    position: absolute; left: 70px; top: 142px;
    display: flex; align-items: center; gap: 22px;
  }
  .brand__square {
    width: 28px; height: 28px;
    background: var(--navy); flex: none;
  }
  .brand__name {
    font-family: "Arimo", sans-serif; font-weight: 400;
    color: var(--navy);
    font-size: 34px; line-height: 1.2;
  }

  /* Back */
  .card--back { left: 760px; top: 150px; width: 370px; height: 572px; }
  .contact-list {
    position: absolute; left: 28px; top: 44px;
    list-style: none;
    font-family: "Arimo", sans-serif; font-size: 14px; color: var(--grey-dark);
    line-height: 1.3;
  }
  .contact-list li { display: flex; align-items: center; justify-content: flex-end; gap: 6px; }
  .contact-list .label { letter-spacing: 0.5px; }
  .contact-list .bullet { width: 6px; height: 6px; border-radius: 50%; background: var(--grey); }
  .contact-list .number { width: 92px; }
  .back-mark {
    position: absolute; right: 28px; top: 44px;
    display: flex; align-items: center; gap: 8px;
  }
  .back-mark__square { width: 14px; height: 14px; background: var(--navy); }
  .back-mark__name { font-family: "Arimo", sans-serif; color: var(--navy); font-size: 18px; }
  .person {
    position: absolute; left: 168px; top: 360px;
    font-family: "Arimo", sans-serif; color: var(--grey-dark);
    font-size: 14px; line-height: 1.45; font-style: normal;
  }
  .person__name {
    font-family: "Libre Baskerville", serif; font-weight: 700;
    color: var(--navy); font-size: 17px; margin-bottom: 2px;
  }
  .band {
    position: absolute; left: 0; right: 0; bottom: 0; height: 92px;
    background: var(--navy);
  }
</style>
</head>
<body>
  <section class="card card--front" aria-label="Card front">
    <svg class="corners" width="580" height="375" viewBox="0 0 580 375" aria-hidden="true">
      <rect width="580" height="375" fill="var(--navy)"/>
      <ellipse cx="290" cy="187" rx="318" ry="210" fill="var(--paper)"/>
    </svg>
    <div class="brand">
      <span class="brand__square" aria-hidden="true"></span>
      <h1 class="brand__name">Tall Maple<br>Communication Solutions</h1>
    </div>
  </section>

  <section class="card card--back" aria-label="Card back">
    <ul class="contact-list">
      <li><span class="label">OFFICE</span><span class="bullet"></span><span class="number">555.214.3080</span></li>
      <li><span class="label">CELL</span><span class="bullet"></span><span class="number">555.836.1942</span></li>
      <li><span class="label">24/7</span><span class="bullet"></span><span class="number">555.407.2261</span></li>
      <li><span class="label">FAX</span><span class="bullet"></span><span class="number">555.690.4518</span></li>
    </ul>
    <div class="back-mark">
      <span class="back-mark__square" aria-hidden="true"></span>
      <span class="back-mark__name">Tall Maple</span>
    </div>
    <address class="person">
      <p class="person__name">Marcus Ellery</p>
      <p>1840 W Juniper Avenue</p>
      <p>Suite 410</p>
      <p>Mesa, AZ 85201</p>
    </address>
    <div class="band"></div>
  </section>
</body>
</html>
```